Agent Recruiting Package

Redesign of our basic real estate agent recruiting brochure. The design can be several pages long and should incorporate all of the elements in the attached document. Additional information can be added at the designers discretion. Ideally I would like it to be more eye catching so it should probably have more images then the attached design.
The "About Us" should be shortened to the version attached in the word document.
Tourview Hub graphics can be found at http://www.tourviewhub-example.com/Resources/GraphicResources.aspx
Ideally final files should be editable by me (someone who does not have access to high end adobe graphic programs). I do have access to Microsoft Publisher and if the best design is only available in Adobe I will work with it.
Please feel free to submit questions. Also make any changes to design, wording, layout, etc. that you feel make a better overall document.
Target Market(s)
Agents currently working for other real estate borkers and new agents just joining the real estate business
Industry/Entity Type
Real Estate
Look and feel

```html
<!DOCTYPE html>
<html lang="en">
<head>
<meta charset="utf-8">
<title>Agent Recruiting Brochure – Spread 4–5</title>
<link href="https://fonts.googleapis.com/css2?family=Anton&family=Oswald:wght@500;600;700&family=Arimo:wght@400;700&display=swap" rel="stylesheet">
<style>
  :root{
    --backdrop:#555555;
    --paper:#ffffff;
    --brand-red:#9b2d3a;
    --brand-red-dark:#7e1f2b;
    --ink:#111111;
    --text:#222222;
    --muted:#666666;
    --sky-top:#d9e6ef;
    --sky-bottom:#b9cbd8;
    --studio-top:#e9eef2;
    --studio-bottom:#b6c6d2;
    --list-row:rgba(215,215,215,.82);
  }
  *{box-sizing:border-box;margin:0;padding:0}
  html,body{width:1200px;height:900px;overflow:hidden}
  body{background:var(--backdrop);font-family:"Arimo",Arial,sans-serif;color:var(--text);position:relative}

  .page{position:absolute;top:83px;height:735px;background:var(--paper);overflow:hidden}
  .page--left{left:32px;width:566px}
  .page--right{left:602px;width:566px}

  /* left page */
  .hero-photo{position:absolute;left:0;top:0;width:566px;height:392px;
    background:linear-gradient(90deg,#c7d8e4 0%,#e8eff4 45%,#9fb4c6 70%,#dfe8ee 100%)}
  .hero-figure{position:absolute;left:340px;top:25px;width:200px;height:367px;
    background:linear-gradient(180deg,#2c3a52,#1d2740);border-radius:60px 60px 0 0;opacity:.85}
  .plan-text{position:absolute;left:32px;top:35px;width:260px}
  .page-title{font-family:"Anton",Impact,sans-serif;font-size:33px;color:var(--brand-red);letter-spacing:.3px;line-height:1;font-weight:400}
  .plan-text .page-title{font-size:31px;margin-bottom:13px;width:300px}
  .plan-text p{font-size:9.4px;line-height:15.4px;color:#1a1a1a;text-align:justify}

  .studio-photo{position:absolute;left:0;top:392px;width:566px;height:343px;
    background:radial-gradient(ellipse at 50% 30%,var(--studio-top),var(--studio-bottom))}
  .person{position:absolute;background:linear-gradient(180deg,#3a3a3c,#161618);border-radius:70px 70px 0 0}
  .person--experienced{left:40px;top:460px;width:160px;height:275px}
  .person--new{left:305px;top:460px;width:130px;height:275px}

  .plan-card{position:absolute;width:143px}
  .plan-card--experienced{left:123px;top:562px}
  .plan-card--new{left:390px;top:562px}
  .plan-card h3{height:40px;background:linear-gradient(180deg,#d8a0a6,var(--brand-red) 70%);
    font-family:"Oswald",sans-serif;font-weight:700;font-size:13px;line-height:14px;color:#111;
    text-align:center;padding-top:6px;text-transform:uppercase}
  .plan-card ul{list-style:none;background:var(--list-row);padding:2px 0 6px}
  .plan-card li{font-size:9px;line-height:11px;color:#222;padding:3px 4px 4px 22px;position:relative;border-bottom:1px solid rgba(255,255,255,.7)}
  .plan-card li:last-child{border-bottom:none}
  .plan-card li svg{position:absolute;left:7px;top:3px}

  .folio{position:absolute;top:702px;font-size:8px;letter-spacing:.4px;color:#555}
  .folio b{font-family:"Oswald",sans-serif;font-size:14px;color:#333;vertical-align:-2px}
  .folio--left{left:34px}
  .folio--left b{margin-right:4px}
  .folio--right{right:32px}
  .folio--right b{margin-left:10px}

  /* right page */
  .commission-title{position:absolute;left:32px;top:30px}
  .intro{position:absolute;left:32px;top:79px;font-size:9.4px;line-height:15px;color:#1a1a1a}
  .handshake-photo{position:absolute;left:32px;top:124px;width:307px;height:124px;
    background:linear-gradient(90deg,#5d6f82,#cfd8df 45%,#e6b99c 60%,#7d8b99)}
  .earning-callout{position:absolute;left:339px;top:124px;width:195px;height:124px;background:var(--brand-red);
    color:#fff;font-family:"Oswald",sans-serif;font-weight:600;padding:10px 0 0 28px;line-height:18px;font-size:14.5px}
  .earning-callout .amount{display:block;font-size:26px;line-height:28px;font-weight:700}

  .ledger{position:absolute;width:185px}
  .ledger--other{left:32px;top:288px}
  .ledger--ours{left:309px;top:288px}
  .ledger--costs{left:32px;top:444px}
  .ledger-caption{font-size:10px;color:#222;margin-bottom:22px}
  .ledger-row{font-family:"Oswald",sans-serif;font-weight:700;font-size:15px;color:#111;
    height:24px;line-height:24px;border-bottom:1px solid #888;padding-left:18px;position:relative}
  .ledger-row .sign{position:absolute;left:4px}
  .ledger-total{font-family:"Anton",Impact,sans-serif;font-size:31px;line-height:40px;height:42px;
    padding-left:18px;border-bottom:2px solid #111;color:#111}
  .ledger--ours .ledger-total{color:var(--brand-red)}
  .ledger--costs .ledger-total{font-size:24px}

  .question{position:absolute;left:32px;top:574px;font-size:15.5px;line-height:20px;color:var(--brand-red)}
  .closing{position:absolute;left:32px;top:631px;font-size:10.4px;line-height:18px;color:#1a1a1a}
</style>
</head>
<body>
  <section class="page page--left">
    <div class="hero-photo" role="img" aria-label="Photo of a businessman in a navy suit standing by a bright office window"></div>
    <div class="hero-figure" role="img" aria-label="Businessman silhouette"></div>
    <div class="plan-text">
      <h1 class="page-title">WHAT’S THE PLAN?</h1>
      <p>All of our agents will eventually earn 100% commission, however agents with less experience will require more help and attention from the office staff and broker therefore they will start in the new agent plan. Any agent with less than three closed transactions (with any New York broker) in the prior two years will be considered a “New Agent”. Once a “new Agent” closes three transactions they will be automatically transitioned to 100% commission.</p>
    </div>

    <div class="studio-photo" role="img" aria-label="Studio photo of a smiling businesswoman holding a house-shaped ruler and a young businessman offering a handshake"></div>
    <div class="person person--experienced" role="img" aria-label="Businesswoman in a dark suit"></div>
    <div class="person person--new" role="img" aria-label="Young businessman reaching out his hand"></div>

    <div class="plan-card plan-card--experienced">
      <h3>Experienced<br>Agents</h3>
      <ul>
        <li><svg width="9" height="9" viewBox="0 0 9 9"><rect width="9" height="9" fill="#fff" stroke="#999" stroke-width=".6"/><path d="M1.5 4.5l2 2 4-5" stroke="#b21f2d" stroke-width="1.6" fill="none"/></svg>$350 Per Month</li>
        <li><svg width="9" height="9" viewBox="0 0 9 9"><rect width="9" height="9" fill="#fff" stroke="#999" stroke-width=".6"/><path d="M1.5 4.5l2 2 4-5" stroke="#b21f2d" stroke-width="1.6" fill="none"/></svg>No Split - You Keep 100%</li>
        <li><svg width="9" height="9" viewBox="0 0 9 9"><rect width="9" height="9" fill="#fff" stroke="#999" stroke-width=".6"/><path d="M1.5 4.5l2 2 4-5" stroke="#b21f2d" stroke-width="1.6" fill="none"/></svg>No Transaction Fees</li>
        <li><svg width="9" height="9" viewBox="0 0 9 9"><rect width="9" height="9" fill="#fff" stroke="#999" stroke-width=".6"/><path d="M1.5 4.5l2 2 4-5" stroke="#b21f2d" stroke-width="1.6" fill="none"/></svg>Free Signs for Listings within the First 10 Days</li>
      </ul>
    </div>

    <div class="plan-card plan-card--new">
      <h3>New<br>Agents</h3>
      <ul>
        <li><svg width="9" height="9" viewBox="0 0 9 9"><rect width="9" height="9" fill="#fff" stroke="#999" stroke-width=".6"/><path d="M1.5 4.5l2 2 4-5" stroke="#b21f2d" stroke-width="1.6" fill="none"/></svg>$35 Per Month</li>
        <li><svg width="9" height="9" viewBox="0 0 9 9"><rect width="9" height="9" fill="#fff" stroke="#999" stroke-width=".6"/><path d="M1.5 4.5l2 2 4-5" stroke="#b21f2d" stroke-width="1.6" fill="none"/></svg>90/10 Split</li>
        <li><svg width="9" height="9" viewBox="0 0 9 9"><rect width="9" height="9" fill="#fff" stroke="#999" stroke-width=".6"/><path d="M1.5 4.5l2 2 4-5" stroke="#b21f2d" stroke-width="1.6" fill="none"/></svg>No Transaction Fees</li>
        <li><svg width="9" height="9" viewBox="0 0 9 9"><rect width="9" height="9" fill="#fff" stroke="#999" stroke-width=".6"/><path d="M1.5 4.5l2 2 4-5" stroke="#b21f2d" stroke-width="1.6" fill="none"/></svg>One on one Guidance any time you need it</li>
      </ul>
    </div>

    <div class="folio folio--left"><b>4</b>ASHGROVE REALTY, LLC</div>
  </section>

  <section class="page page--right">
    <h1 class="page-title commission-title">KEEP MORE OF YOUR COMMISSION</h1>
    <p class="intro">Let’s assume you close 4 transaction sides next year with an average sale price<br>of $420,000 and an average commission of 2%.</p>

    <div class="handshake-photo" role="img" aria-label="Close-up photo of two businessmen shaking hands"></div>
    <div class="earning-callout">That’s a commission<br>earning of<span class="amount">$33,600.</span>How much<br>will you keep?</div>

    <div class="ledger ledger--other">
      <p class="ledger-caption">With another broker at 70/30 split:</p>
      <div class="ledger-row">$33,600</div>
      <div class="ledger-row"><span class="sign">-</span>$10,080 to broker</div>
      <div class="ledger-total">$23,520</div>
    </div>

    <div class="ledger ledger--ours">
      <p class="ledger-caption">With Ashgrove Realty:</p>
      <div class="ledger-row">$33,600</div>
      <div class="ledger-row"><span class="sign">-</span>$4,200</div>
      <div class="ledger-total">$29,400</div>
    </div>

    <div class="ledger ledger--costs">
      <div class="ledger-row">E &amp; O</div>
      <div class="ledger-row"><span class="sign">-</span>Marketing Costs</div>
      <div class="ledger-row">Tourview Hub</div>
      <div class="ledger-total">?</div>
    </div>

    <p class="question">Now consider, this is an example of average.<br>What happens if you are above average?</p>
    <p class="closing">At Ashgrove Realty we take nothing more. You pay $350 per month… period.<br>You are rewarded for your hard work by earning even more money. Other brokers<br>reward themselves putting more of your hard earned money in their pocket.</p>

    <div class="folio folio--right">ASHGROVE REALTY, LLC<b>5</b></div>
  </section>
</body>
</html>
```